Paw Summit Co business card

I need a business card design for a dog training company in Toronto called Paw Summit Co. My training is unique, outdoor training that helps people create a better bond with their dog through communication and understanding their dog's true nature. I do not use treats - but communication and praise for the dog.

I help people create a better life for them and their dog. From puppy training right through to seniors, I offer both group classes called Curbside Poise Course as well as in-home private sessions.

I believe that having a dog is a lifestyle, so I encourage clients to incorporate their dog into their active life. Outdoor activities such as hiking, mental stimulation, proper care and healthy food for their dog are all keys to a healthy and happy dog.

I would like a fresh and modern look that works with my logo. I would like to convey fun, confidence and happiness.

My services are premium services. I am a Certified Dog Trainer, and offer value for money, but my prices are higher than other trainers.
Updates

Thank you to everyone who submitted designs! I'm so impressed with the level of creativity and the options that you all have given me. It will be a difficult choice for sure. As this was my first experience with Art Huddle - it has been a great one.

maren.

Industry/Entity Type

Communication

Requirements
Must have
• Maren Quill, CTE
Certified Trainer Educator
maren@pawsummitco.ca
555-318-0472
pawsummitco.ca

Prefer a double sided card.
Must have Paw Summit Co logo. File attached. I do have a stroke logo for a dark background as well.

Must only use the fonts and colours as outlined in my brand guidelines, which are attached.
Should not have
• no cheesy pet images
do not use the tongue as an element outside of the logo
minimize the use of pink - can be used as an accent colour but should not be a main colour

```html
<!DOCTYPE html>
<html lang="en">
<head>
<meta charset="utf-8">
<title>Paw Summit Co business card</title>
<link rel="stylesheet" href="https://fonts.googleapis.com/css2?family=Questrial&display=swap">
<style>
  :root {
    --page-bg: #ece9e4;
    --blue-light: #2aaee0;
    --blue-dark: #0d86bd;
    --grid-on-blue: rgba(255, 255, 255, 0.22);
    --grid-on-white: #cfe6f0;
    --card-white: #ffffff;
    --card-shade: #eef1f2;
    --brand-green: #8cbf3f;
    --ink: #2f2f2f;
    --ink-soft: #4a4a4a;
    --white: #ffffff;
  }
  * { margin: 0; padding: 0; box-sizing: border-box; }
  html, body {
    width: 1200px;
    height: 923px;
    overflow: hidden;
    background: var(--page-bg);
    font-family: "Questrial", "Century Gothic", sans-serif;
  }
  .sheet {
    position: relative;
    width: 1200px;
    height: 923px;
  }
  .card {
    position: absolute;
    top: 305px;
    width: 540px;
    height: 312px;
    border-radius: 4px;
    overflow: hidden;
    box-shadow: 0 8px 24px rgba(0, 0, 0, 0.18);
  }
  .card-front {
    left: 40px;
    background:
      linear-gradient(var(--grid-on-blue) 1px, transparent 1px) 0 0 / 45px 39px,
      linear-gradient(90deg, var(--grid-on-blue) 1px, transparent 1px) 0 0 / 45px 39px,
      radial-gradient(ellipse at 50% 45%, var(--blue-light), var(--blue-dark));
  }
  .card-back {
    left: 620px;
    background:
      linear-gradient(var(--grid-on-white) 1px, transparent 1px) 0 0 / 45px 39px,
      linear-gradient(90deg, var(--grid-on-white) 1px, transparent 1px) 0 0 / 45px 39px,
      radial-gradient(ellipse at 55% 40%, var(--card-white), var(--card-shade));
  }
  .brand-name {
    position: absolute;
    font-size: 34px;
    line-height: 1;
    letter-spacing: 0.5px;
    white-space: nowrap;
  }
  .card-front .brand-name {
    left: 50%;
    top: 118px;
    transform: translateX(-50%);
    color: var(--white);
  }
  .card-back .brand-name {
    right: 46px;
    top: 62px;
    font-size: 30px;
    color: var(--ink);
  }
  .front-url {
    position: absolute;
    left: 50%;
    top: 186px;
    transform: translateX(-50%);
    color: var(--white);
    font-size: 13px;
    letter-spacing: 7px;
    white-space: nowrap;
  }
  .person {
    position: absolute;
    left: 30px;
    top: 30px;
  }
  .person-line {
    display: flex;
    align-items: baseline;
    gap: 18px;
  }
  .person-name {
    color: var(--brand-green);
    font-size: 26px;
  }
  .person-credential {
    color: var(--ink);
    font-size: 13px;
  }
  .person-title {
    margin-top: 6px;
    color: var(--ink);
    font-size: 13px;
  }
  .contact {
    position: absolute;
    left: 30px;
    bottom: 26px;
    color: var(--ink-soft);
    font-size: 12.5px;
    line-height: 1.7;
  }
  .contact-url {
    color: var(--brand-green);
    letter-spacing: 6px;
    font-size: 13px;
  }
</style>
</head>
<body>
<main class="sheet">
  <section class="card card-front" aria-label="Card front">
    <div class="brand-name">Paw Summit Co</div>
    <div class="front-url">www.pawsummitco.ca</div>
  </section>

  <section class="card card-back" aria-label="Card back">
    <div class="brand-name">Paw Summit Co</div>
    <div class="person">
      <div class="person-line">
        <span class="person-name">Maren Quill</span>
        <span class="person-credential">CTE</span>
      </div>
      <div class="person-title">Certified Trainer Educator</div>
    </div>
    <div class="contact">
      <div class="contact-line">P: 555-318-0472, E: maren@pawsummitco.ca</div>
      <div class="contact-line">#1321, Your Street, Your Location, Your Town, Your Country</div>
      <div class="contact-url">www.pawsummitco.ca</div>
    </div>
  </section>
</main>
</body>
</html>
```